Improve the existing label for Zentroluxiva company.

The ZLV company is launching a new product and needs the label for the product to be re-designed. Candidates should maintain the actual texts, and see if they can improve on the PuraVetrix Logo and the Biodegradable logo.
For the PuraVetrix Logo please use a diamond (any diamont will suffice)
The label should maintain the blue on white aspect and can use blue gradients.(monochromatic).
the white part of the label and the bottle will be transparent, and the liquid inside the bottle is blue.

The product is a monitor/tv/cell/tablet screen cleaner.
The label size is (7 cm in heigh)t and (3,8 cm in lenght).

The actual label is attached.

Thanks in advance for your designs.

```html
<!DOCTYPE html>
<html lang="pt-BR">
<head>
<meta charset="utf-8">
<title>PuraVetrix – Linha Aqua</title>
<link href="https://fonts.googleapis.com/css2?family=Arimo:wght@700&family=Righteous&display=swap" rel="stylesheet">
<style>
  :root {
    --brand-blue: #3f3c8f;
    --label-white: #ffffff;
  }
  * { margin: 0; padding: 0; box-sizing: border-box; }
  html, body {
    width: 1200px;
    height: 2204px;
    overflow: hidden;
    background: var(--label-white);
  }
  .label {
    position: relative;
    width: 1200px;
    height: 2204px;
    background: var(--label-white);
    color: var(--brand-blue);
  }
  .brand-name {
    position: absolute;
    top: 92px;
    left: 0;
    width: 100%;
    text-align: center;
    font-family: "Arimo", Arial, sans-serif;
    font-weight: 700;
    font-size: 196px;
    line-height: 150px;
    letter-spacing: -2px;
    color: var(--brand-blue);
  }
  .line-band {
    position: absolute;
    top: 514px;
    left: 0;
    width: 100%;
    height: 205px;
    background: var(--brand-blue);
    display: flex;
    align-items: center;
    justify-content: center;
  }
  .line-band h2 {
    font-family: "Righteous", "Arial Rounded MT Bold", sans-serif;
    font-weight: 400;
    font-size: 98px;
    letter-spacing: 6px;
    color: var(--label-white);
  }
  .eco-badge {
    position: absolute;
    top: 808px;
    left: 412px;
    width: 380px;
    height: 380px;
  }
  .usage {
    position: absolute;
    top: 1284px;
    left: 0;
    width: 100%;
    text-align: center;
    font-family: "Righteous", "Arial Rounded MT Bold", sans-serif;
    font-weight: 400;
    font-size: 80px;
    line-height: 117px;
    letter-spacing: 0;
    color: var(--brand-blue);
  }
  .volume-band {
    position: absolute;
    top: 1917px;
    left: 0;
    width: 100%;
    height: 287px;
    background: var(--brand-blue);
    display: flex;
    align-items: center;
    justify-content: center;
  }
  .volume-band p {
    font-family: "Arimo", Arial, sans-serif;
    font-weight: 700;
    font-size: 62px;
    letter-spacing: 2px;
    color: var(--label-white);
  }
</style>
</head>
<body>
  <main class="label">
    <h1 class="brand-name">Pura<br>Vetrix</h1>

    <section class="line-band">
      <h2>LINHA AQUA</h2>
    </section>

    <svg class="eco-badge" viewBox="0 0 380 380" role="img" aria-label="Selo de produto biodegradável e ecológico">
      <circle cx="190" cy="190" r="180" fill="none" stroke="var(--brand-blue)" stroke-width="16"/>
      <circle cx="190" cy="190" r="150" fill="none" stroke="var(--brand-blue)" stroke-width="6"/>
    </svg>

    <p class="usage">
      PARA LIMPEZA DE<br>
      MONITORES - TV - LCD<br>
      LED - PLASMA - ÓCULOS<br>
      CAMERAS - TABLETS<br>
      CELULARES
    </p>

    <footer class="volume-band">
      <p>CONTÉM 60 ml</p>
    </footer>
  </main>
</body>
</html>
```